【依頼の目的/概要】
電子書籍(vellis)の表紙デザインをお願いします。

【画像サイズ】 ※VSRより抜粋
表紙ファイルの理想的な寸法 2,560×1,600ピクセルです。
注:画像の寸法は 1,000×625ピクセル以上であることが必要です。
画像の最大の寸法は 10,000×10,000ピクセルです。

【タイトル】

港町の料理人へ贈る
季節ごとに変わる庭の手入れがわかる
「月灯り菜園ノート」

【著者】

MIRO

【本の内容】

5つの窓辺・ロカルナ年代記などの人間心理・成功本から
パートナーに関する知識をまとめて解説した本です。

※本文を参考資料として添付します。

【デザイン要望】

特にイメージにこだわりはありませんので、
自由な発送でのデザインご応募を楽しみにしています。

※次点、次々点の方への参加報酬を設定致しました。

※その他 必要な情報がありましたら、お問い合わせください。

ターゲット層がリアル風が好きだと思ったので、選びました

今回も多数応募頂きまして、誠にありがとうございました。

```html
<!DOCTYPE html>
<html lang="ja">
<head>
<meta charset="utf-8">
<title>港町の料理人へ贈る 月灯り菜園ノート</title>
<link href="https://fonts.googleapis.com/css2?family=Noto+Sans+JP:wght@500;700;900&display=swap" rel="stylesheet">
<style>
  :root {
    --navy: #1d3d86;
    --red: #e3263f;
    --blue: #2f72d6;
    --ink: #141414;
    --paper: #ffffff;
    --device: #1b1b1b;
    --marker: #ffd1d7;
    --dot: #f2c200;
  }
  * { margin: 0; padding: 0; box-sizing: border-box; }
  html, body { width: 750px; height: 1200px; overflow: hidden; background: var(--paper); }
  body { font-family: "Noto Sans JP", sans-serif; color: var(--ink); }
  p, h1 { line-height: 1.2; }
  .cover { position: relative; width: 750px; height: 1200px; background: var(--paper); overflow: hidden; }

  .audience-marks { position: absolute; top: 30px; left: 0; }
  .audience { position: absolute; top: 34px; left: 0; width: 750px; text-align: center; font-weight: 900; font-size: 58px; color: var(--navy); }

  .subtitle-a { position: absolute; top: 124px; left: 0; width: 750px; text-align: center; font-weight: 900; font-size: 48px; color: var(--red); }
  .subtitle-b { position: absolute; top: 186px; left: 0; width: 750px; text-align: center; font-weight: 900; font-size: 52px; color: var(--ink); }
  .emph-dot { position: relative; }
  .emph-dot::before { content: ""; position: absolute; top: -2px; left: 50%; width: 8px; height: 8px; margin-left: -4px; border-radius: 50%; background: var(--dot); }

  .title-main { position: absolute; top: 252px; left: 0; width: 750px; text-align: center; font-weight: 900; font-size: 92px; line-height: 1.1; letter-spacing: -2px; }
  .title-main .moon { color: var(--red); }
  .title-main .garden { color: var(--blue); }
  .title-sub { position: absolute; top: 354px; left: 190px; font-weight: 900; font-size: 62px; line-height: 1.1; color: var(--ink); }
  .author { position: absolute; top: 356px; left: 470px; }
  .author-role { font-weight: 700; font-size: 20px; color: var(--ink); }
  .author-name { font-weight: 900; font-size: 44px; line-height: 1.05; color: var(--ink); letter-spacing: 2px; }

  .illustration { position: absolute; top: 436px; left: 30px; width: 690px; height: 360px; border-radius: 30px;
    background: radial-gradient(ellipse at 50% 50%, #f6d05a 0%, #f1b93d 18%, #cfe0f5 42%, #e8f0fa 70%, #ffffff 100%); }

  .device { position: absolute; top: 800px; left: 12px; width: 250px; height: 390px; background: var(--device); border-radius: 22px; }
  .device-screen { position: absolute; top: 20px; left: 16px; width: 218px; height: 310px; background: var(--paper); padding: 14px 8px; text-align: center; }
  .device-button { position: absolute; bottom: 14px; left: 50%; width: 30px; height: 30px; margin-left: -15px; border-radius: 50%; background: #444; }
  .device-screen p { font-weight: 900; line-height: 1.3; }
  .gift-lead { font-size: 26px; }
  .gift-body { font-size: 19px; margin-top: 6px; }
  .gift-test { font-size: 21px; margin-top: 6px; }
  .gift-end { font-size: 21px; margin-top: 6px; }
  .gift-end .mark { color: var(--red); }

  .message { position: absolute; top: 915px; left: 275px; width: 465px; height: 272px; background: var(--paper); padding: 12px 10px; }
  .message-cause { font-weight: 900; font-size: 26px; line-height: 1.45; color: var(--ink); }
  .message-cause span { background: linear-gradient(transparent 62%, var(--marker) 62%); }
  .message-call { margin-top: 10px; font-weight: 900; line-height: 1.35; }
  .call-lead { text-align: right; font-size: 20px; }
  .call-lead .scale { display: inline-block; background: var(--red); color: var(--paper); padding: 0 5px; font-size: 28px; line-height: 1.2; }
  .call-main { font-size: 27px; color: var(--red); white-space: nowrap; }
  .call-end { text-align: right; font-size: 20px; }
</style>
</head>
<body>
<main class="cover">
  <svg class="audience-marks" width="750" height="100" viewBox="0 0 750 100" aria-hidden="true">
    <g stroke="var(--ink)" stroke-width="6" stroke-linecap="round">
      <line x1="56" y1="22" x2="74" y2="52"/><line x1="36" y1="40" x2="66" y2="66"/>
      <line x1="694" y1="22" x2="676" y2="52"/><line x1="714" y1="40" x2="684" y2="66"/>
    </g>
  </svg>
  <p class="audience">港町の料理人へ贈る</p>
  <p class="subtitle-a">季節<span class="emph-dot">ご</span><span class="emph-dot">と</span><span class="emph-dot">に</span>変わる</p>
  <p class="subtitle-b">庭の手入れがわかる</p>
  <h1 class="title-main">「<span class="moon">月灯り</span><span class="garden">菜園</span>」</h1>
  <p class="title-sub">ノート</p>
  <div class="author">
    <p class="author-role">メンタルトレーナー</p>
    <p class="author-name">MIRO</p>
  </div>

  <div class="illustration" role="img" aria-label="大きな電球の中のハートを中心に、青い円と赤い矢印で結ばれた人物たちのイラスト"></div>

  <aside class="device">
    <div class="device-screen">
      <p class="gift-lead">ルミナ登録で</p>
      <p class="gift-body">右脳・左脳、男性、<br>女性の機能で判断</p>
      <p class="gift-test">『あなたの<br>パーソナリティ<br>分析』テストを</p>
      <p class="gift-end"><span class="mark">読者限定</span>プレゼント</p>
    </div>
    <span class="device-button"></span>
  </aside>

  <section class="message">
    <p class="message-cause"><span>メンタル不調を起こしている人の真の原因は、家庭・パートナーとの関係の破綻。</span></p>
    <div class="message-call">
      <p class="call-lead">目から<span class="scale">鱗</span>の</p>
      <p class="call-main">視点を変えてのパートナー選び</p>
      <p class="call-end">をしてみよう!</p>
    </div>
  </section>
</main>
</body>
</html>
```